Webpage design for a translation agancy

We need to update and modernize our current Wordpress webpage www.verbanova.se. I am happy with the basics but there are definitely room for an update.
We are a translation agency providing translation services B2B. We supply translations to different industries. Law, HR, Medical, Financial, IT, Technical, Business. Our clients are mostly Swedish based companies.
We would like to see designs that:
- Increases our conversions
- Conveys reliance to our visitors/clients
- Keeps the framework on our current webpage (more or less)
- The quote bottom and quotation form is a crucial for our business. Drag and drop is a must.
-We'd like to keep the banner pics. One of them is our view from our office and the two others are local pictures from Stockholm/Sweden. The banner and the quote has to be integrated in the update.
-The design has to include designs for the whole webpage, landing page and all other pages.
/Teodor
Target Market(s)
Our target market is Swedish companies, b2b, operating in different industries. Law, Finance, Medical, IT, HR, Marketing, Engineering. Only B2B. Our typical buyer is a decision maker/ middle management.
Requirements
Must have
- - Conveys reliance to our visitors/clients
- - Our current Unique Selling Points
- - Keeps the framework on our current webpage (more or less)
- - The quote bottom and quotation form is a crucial for our business. One compeditor whom has a good solution for the quote form is, www.lingmarka.lv/en/
- -We'd like to keep the banner pics. One of them is our view from our office and the two others are local pictures from Stockholm/Sweden. The banner and the quote has to be integrated in the update.
- -The design has to include designs for the whole webpage, landing page and all other pages.
Nice to have
- Pretty much same color scales as today.

```html
<!DOCTYPE html>
<html lang="en">
<head>
<meta charset="utf-8">
<title>Verbanova – Translation Agency</title>
<link href="https://fonts.googleapis.com/css2?family=Open+Sans:wght@300;400;600;700&display=swap" rel="stylesheet">
<style>
:root{
  --purple:#9d5fd6;
  --purple-dark:#8a4cc6;
  --green:#8cc63f;
  --blue:#5d86d6;
  --sky:#6cb5d6;
  --ink:#333;
  --muted:#666;
  --light:#eceeee;
  --line:#dcdcdc;
  --white:#fff;
  --icon:#6fb4d2;
}
*{box-sizing:border-box;margin:0;padding:0}
html,body{width:1200px;height:4082px;overflow:hidden}
body{font-family:"Open Sans",Arial,sans-serif;color:var(--ink);background:var(--white);position:relative}
.abs{position:absolute}
.rainbow{height:5px;background:linear-gradient(90deg,#8cc63f 0 20%,#6cb5d6 20% 40%,#9d5fd6 40% 60%,#f0a030 60% 80%,#e05a8a 80%)}
/* utility */
.utility{top:5px;left:0;width:1200px;height:31px;display:flex;justify-content:flex-end;gap:22px;padding-right:160px;align-items:center;font-size:12px;color:var(--muted);white-space:nowrap}
.utility span{display:flex;align-items:center;gap:5px}
.utility i{width:9px;height:9px;background:#777;border-radius:2px;display:inline-block}
/* nav */
.nav{top:36px;left:0;width:1200px;height:100px;display:flex;align-items:center;padding:0 160px;border-top:1px solid #eee}
.brand{font-size:34px;font-weight:700;color:#555;letter-spacing:.5px;display:flex;align-items:center;gap:8px;white-space:nowrap}
.brand b{width:14px;height:14px;border-radius:50%;background:var(--green);display:inline-block}
.menu{margin-left:auto;display:flex;gap:30px;font-size:13px;color:#444;white-space:nowrap}
/* hero */
.hero{top:136px;left:0;width:1200px;height:526px;background:linear-gradient(180deg,#5e646a 0%,#c9ced2 35%,#e4e6e8 60%,#9aa0a6 100%)}
.hero-tag{top:346px;left:0;width:653px;height:105px;background:var(--purple);opacity:.93;color:#fff;font-size:28px;font-weight:600;display:flex;align-items:center;padding-left:180px;letter-spacing:.5px;white-space:nowrap}
.arrow{top:378px;width:30px;height:40px}
.btn-quote{top:640px;left:498px;width:204px;height:50px;background:var(--green);color:#fff;font-weight:600;font-size:17px;display:flex;align-items:center;justify-content:center;z-index:2;letter-spacing:.3px}
/* quote */
.quote{top:662px;left:0;width:1200px;height:399px;background:var(--light)}
.close-box{top:62px;left:1012px;width:25px;height:25px;background:var(--green);color:#fff;font-size:14px;display:flex;align-items:center;justify-content:center}
.quote h2{position:absolute;top:100px;left:160px;font-size:23px;font-weight:400;color:#333}
.quote .note{position:absolute;top:136px;left:160px;font-size:12px;font-style:italic;color:#555}
.field{position:absolute;background:#fff;border:1px solid #e2e2e2;font-size:12px;color:#555;padding:12px 14px}
.upload{display:flex;align-items:center;gap:18px;padding-left:20px}
.captcha{position:absolute;top:173px;left:808px;width:232px;height:62px;background:#f9f9f9;border:1px solid #d3d3d3;display:flex;align-items:center;padding:0 12px;gap:12px;font-size:12px}
.captcha i{width:24px;height:24px;border:2px solid #c1c1c1;background:#fff}
.captcha em{margin-left:auto;width:28px;height:28px;background:#c7d3e6;border-radius:4px}
.badge{position:absolute;top:243px;left:808px;display:flex;gap:10px;align-items:center;font-size:9px;color:#555}
.badge i{width:26px;height:34px;background:#cfd6e2;border-radius:3px}
.badge b{width:26px;height:26px;border-radius:50%;background:#bfc4c8}
.send{position:absolute;top:309px;left:808px;width:90px;height:39px;background:var(--green);color:#fff;font-weight:600;font-size:14px;display:flex;align-items:center;justify-content:center}
/* about */
.about{top:1061px;left:0;width:1200px;height:416px;background:#fff}
.about h2{position:absolute;top:80px;left:160px;font-size:30px;font-weight:400}
.about .body{position:absolute;top:140px;left:160px;width:565px;font-size:12.5px;line-height:1.72;color:#444}
.about .body p{margin-bottom:14px}
.about-photo{position:absolute;top:0;left:672px;width:528px;height:416px}
/* why */
.why{top:1477px;left:0;width:1200px;height:583px;background:#fff;border-top:1px solid #eee}
.why h2{position:absolute;top:60px;left:160px;font-size:30px;font-weight:400}
.why .lead{position:absolute;top:120px;left:160px;width:520px;font-size:12.5px;line-height:1.7;color:#444}
.feature{position:absolute;width:300px;display:flex;gap:22px}
.feature .ic{flex:none;width:86px;height:86px;border-radius:50%;background:#eef0f1;display:flex;align-items:center;justify-content:center}
.feature h3{font-size:14px;font-weight:600;color:var(--icon);letter-spacing:.5px;margin:6px 0 8px}
.feature p{font-size:11.5px;line-height:1.65;color:#444}
.person{position:absolute;top:26px;left:816px;width:245px;height:557px}
/* industry */
.industry{top:2060px;left:0;width:1200px;height:628px;background:var(--light)}
.industry h2{position:absolute;top:112px;left:160px;font-size:32px;font-weight:400;line-height:1.25}
.industry .lead{position:absolute;top:214px;left:160px;width:200px;font-size:11.5px;line-height:1.7;color:#444}
.tile{position:absolute;width:207px;height:200px;color:#fff;display:flex;flex-direction:column;align-items:center;justify-content:flex-end;padding-bottom:40px;font-size:14px;letter-spacing:1px;gap:26px}
.tile svg{width:64px;height:64px}
.t-green{background:linear-gradient(135deg,#9ccf52,#80bb36)}
.t-blue{background:linear-gradient(135deg,#6b91dc,#4f77c9)}
.t-purple{background:linear-gradient(135deg,#ae78e3,#9258d2)}
.notch{position:absolute;left:560px;width:80px;height:40px}
/* testimonials */
.testi{top:2688px;left:0;width:1200px;height:351px;background:var(--sky)}
.testi h2{position:absolute;top:88px;left:0;width:1200px;text-align:center;color:#fff;font-size:30px;font-weight:300}
.avatar{position:absolute;top:2845px;left:245px;width:104px;height:104px;border-radius:50%;border:4px solid #fff;background:linear-gradient(#7a6a5e,#3e3430)}
.testi .quote-text{position:absolute;top:176px;left:397px;width:645px;color:#fff;font-size:12px;line-height:1.75;font-style:italic}
.testi .who{position:absolute;top:262px;left:397px;color:#fff;font-size:12px;font-weight:700}
.dots{position:absolute;top:293px;left:571px;display:flex;gap:6px}
.dots i{width:12px;height:12px;border-radius:50%;background:rgba(255,255,255,.55)}
.dots i:first-child{background:#fff}
/* news */
.news{top:3039px;left:0;width:1200px;height:625px;background:#fff}
.news h2{position:absolute;top:68px;left:0;width:1200px;text-align:center;font-size:30px;font-weight:400}
.news .lead{position:absolute;top:120px;left:340px;width:520px;text-align:center;font-size:12px;line-height:1.7;color:#444}
.card{position:absolute;top:198px;width:272px}
.card .img{height:171px}
.share{display:flex;gap:10px;margin:28px 0 10px 8px}
.share i{width:10px;height:10px;border-radius:50%;background:var(--blue)}
.card h3{font-size:15px;font-weight:400;margin-bottom:10px}
.card p{font-size:11.5px;line-height:1.6;color:#444}
.card .meta{margin-top:12px;font-size:10.5px;color:var(--purple)}
/* partners */
.partners{top:3664px;left:0;width:1200px;height:109px;background:var(--light);display:flex;justify-content:center;align-items:center;gap:34px}
.partners i{display:block;height:20px;background:#b2b6ba;border-radius:3px}
/* footer */
.footer{top:3778px;left:0;width:1200px;height:304px;background:var(--light)}
.footer .brand{position:absolute;top:40px;left:160px;font-size:30px}
.footer .about-f{position:absolute;top:104px;left:160px;width:200px;font-size:11.5px;line-height:1.7;color:#555}
.col{position:absolute;top:86px;font-size:11.5px;line-height:2.05;color:#555;white-space:nowrap}
.col h4{font-size:12px;font-weight:700;color:#333;margin-bottom:10px;letter-spacing:.5px}
.bottom{position:absolute;top:226px;left:160px;width:880px;border-top:1px solid #d6d6d6}
.soc{position:absolute;top:254px;left:160px;display:flex;gap:8px}
.soc i{width:26px;height:26px;border-radius:50%;background:var(--sky)}
.copy{position:absolute;top:260px;left:690px;font-size:10.5px;color:#555;display:flex;gap:16px;white-space:nowrap}
</style>
</head>
<body>

<div class="abs rainbow" style="top:0;left:0;width:1200px"></div>
<div class="abs utility">
  <span><i></i>Contact us</span>
  <span><i></i>Request a quote!</span>
  <span>Language ▾</span>
  <span><i></i>Interpreter</span>
</div>

<header class="abs nav">
  <div class="brand">verbanova<b></b></div>
  <nav class="menu">
    <span>Our services</span><span>Translation methods</span><span>Customer cases</span><span>About us</span><span>Stockholm</span><span>For Translators</span>
  </nav>
</header>

<section class="abs hero" role="img" aria-label="Banner photo: office interior with large windows overlooking Stockholm"></section>
<div class="abs hero-tag">KVALITET ÄR VIKTIGT FÖR OSS</div>
<svg class="abs arrow" style="left:52px" viewBox="0 0 30 40"><path d="M20 6 L8 20 L20 34" stroke="#fff" stroke-width="3" fill="none"/></svg>
<svg class="abs arrow" style="left:1118px" viewBox="0 0 30 40"><path d="M10 6 L22 20 L10 34" stroke="#fff" stroke-width="3" fill="none"/></svg>
<div class="abs btn-quote">REQUEST QUOTE</div>

<section class="abs quote">
  <div class="abs close-box">×</div>
  <h2>Request a Quote</h2>
  <p class="note">Use the form below for a free cost estimate, or e-mail your request to us at info@verbanova.se</p>
  <div class="field" style="top:173px;left:160px;width:297px;height:40px">Name*:</div>
  <div class="field" style="top:222px;left:160px;width:297px;height:40px">Email*:</div>
  <div class="field" style="top:271px;left:160px;width:297px;height:40px">Phone*:</div>
  <div class="field" style="top:320px;left:160px;width:297px;height:40px">Company*:</div>
  <div class="field" style="top:173px;left:465px;width:335px;height:78px">Comments:</div>
  <div class="field upload" style="top:263px;left:465px;width:335px;height:82px">
    <svg width="58" height="40" viewBox="0 0 58 40"><path d="M14 38 a12 12 0 0 1 0-24 a16 16 0 0 1 30-2 a13 13 0 0 1 0 26z" fill="#5cb3dd"/><path d="M29 32 V18 M23 24 L29 18 L35 24" stroke="#fff" stroke-width="3" fill="none"/></svg>
    <span>Click or drag and drop your file here<br>(Max 40MB)</span>
  </div>
  <div class="captcha"><i></i>I'm not a robot<em></em></div>
  <div class="badge"><i></i><b></b><span>Swedish professional<br>translators</span></div>
  <div class="send">SEND</div>
</section>

<section class="abs about">
  <h2>Verbanova Translation Agency</h2>
  <div class="body">
    <p>Verbanova is a translation agency that provides language services of the highest quality and maintains a strong focus on you, the customer. We assist our customers on a daily basis by translating industry-specific documentation to a wide variety of languages. Our project managers ensure that you receive expert help from our highly qualified specialist translators, who will adapt your text to the relevant target audience.</p>
    <p>Irrespective of whether your project comprises technical manuals, legal documentation, annual reports or websites, we can assist you. Our business concept is to provide translation services with a strong focus on personal service and quality.</p>
    <p>Our goal is always to build long-term partnerships with our customers.</p>
  </div>
  <svg class="about-photo" viewBox="0 0 528 416" role="img" aria-label="Photo: two business people shaking hands, seen from above">
    <defs><linearGradient id="ap" x1="0" y1="0" x2="1" y2="1"><stop offset="0" stop-color="#d6d8da"/><stop offset="1" stop-color="#a9adb1"/></linearGradient></defs>
    <polygon points="0,416 150,0 528,0 528,416" fill="#e9eaeb"/>
    <polygon points="180,416 310,0 528,0 528,416" fill="url(#ap)"/>
  </svg>
</section>

<section class="abs why">
  <h2>Why Us?</h2>
  <p class="lead">Sed ut perspiciatis unde omnis iste natus error sit voluptatem accusantium doloremque laudantium, totam rem aperiam, eaque ipsa quae ab illo inventore veritatis et quasi architecto beata.</p>
  <div class="feature" style="top:200px;left:160px">
    <div class="ic"><svg width="44" height="44" viewBox="0 0 44 44"><circle cx="22" cy="18" r="12" fill="none" stroke="#6fb4d2" stroke-width="3"/><path d="M15 28 L11 42 L18 38 L22 42 L26 38 L33 42 L29 28" fill="#6fb4d2"/></svg></div>
    <div><h3>QUALITY</h3><p>Vi fokuserar på att hålla hög kvalitet i alla delar av översättningsprocessen. Från projektledning, översättning…</p></div>
  </div>
  <div class="feature" style="top:200px;left:498px">
    <div class="ic"><svg width="44" height="44" viewBox="0 0 44 44"><circle cx="22" cy="22" r="17" fill="none" stroke="#6fb4d2" stroke-width="3"/><path d="M22 11 V22 L30 27" stroke="#6fb4d2" stroke-width="3" fill="none"/></svg></div>
    <div><h3>DELIVERY</h3><p>Vi har som mål att mot samtliga våra uppdrag hålla bästa möjliga leveranstid och att leverera i format som.</p></div>
  </div>
  <div class="feature" style="top:338px;left:160px">
    <div class="ic"><svg width="44" height="44" viewBox="0 0 44 44"><path d="M12 40 V30 C4 24 6 6 22 6 C36 6 38 18 34 24 L36 30 H32 V40" fill="none" stroke="#6fb4d2" stroke-width="3"/><circle cx="21" cy="19" r="5" fill="#6fb4d2"/></svg></div>
    <div><h3>COMPETENCE</h3><p>Som översättningsbyrå har vi krav på oss att alltid ligga steget före. Vi jobbar enbart med branschens mest.</p></div>
  </div>
  <div class="feature" style="top:338px;left:498px">
    <div class="ic"><svg width="44" height="44" viewBox="0 0 44 44"><rect x="10" y="20" width="24" height="18" rx="2" fill="#6fb4d2"/><path d="M15 20 V14 a7 7 0 0 1 14 0 V20" fill="none" stroke="#6fb4d2" stroke-width="3"/></svg></div>
    <div><h3>SECRECY</h3><p>Vi behandlar alla våra kunders uppdrag och dokument med högsta krav på säkerhet och sekretess.</p></div>
  </div>
  <div class="person" role="img" aria-label="Photo: smiling businesswoman in a grey suit with arms crossed" style="background:linear-gradient(180deg,#e9e4e0 0%,#8a8e95 45%,#5d6269 100%);border-radius:110px 110px 0 0"></div>
</section>

<section class="abs industry">
  <svg class="notch" style="top:-1px" viewBox="0 0 80 40"><path d="M0 0 Q40 0 40 40 Q40 0 80 0 Z" fill="#fff"/></svg>
  <h2>We know<br>your industry</h2>
  <p class="lead">Sed ut perspiciatis unde omnis iste natus error sit voluptatem. Totam rem aperiam, eaque ipsa quae ab illo inventore veritatis et quasi architecto beata.</p>

  <div class="tile t-green" style="top:108px;left:384px"><svg viewBox="0 0 64 64" fill="none" stroke="#fff" stroke-width="3"><path d="M32 8 V54 M20 56 H44 M10 18 H54"/><path d="M10 18 L4 34 H16 Z M54 18 L48 34 H60 Z" fill="#fff"/></svg>LAW</div>
  <div class="tile t-blue" style="top:108px;left:604px"><svg viewBox="0 0 64 64"><circle cx="32" cy="20" r="11" fill="#fff"/><path d="M12 58 C12 38 52 38 52 58 Z" fill="#fff"/></svg>HR</div>
  <div class="tile t-purple" style="top:108px;left:827px"><svg viewBox="0 0 64 64"><rect x="6" y="16" width="52" height="40" rx="5" fill="#fff"/><path d="M24 16 V10 H40 V16" stroke="#fff" stroke-width="3" fill="none"/><path d="M32 26 V46 M22 36 H42" stroke="#9d5fd6" stroke-width="6"/></svg>MEDICAL</div>

  <div class="tile t-blue" style="top:326px;left:160px"><svg viewBox="0 0 64 64"><path d="M24 8 H40 L36 18 C52 26 54 58 32 58 C10 58 12 26 28 18 Z" fill="#fff"/><text x="32" y="48" text-anchor="middle" font-size="20" font-family="Open Sans,sans-serif" fill="#5d86d6" font-weight="700">$</text></svg>FINANCIAL</div>
  <div class="tile t-purple" style="top:326px;left:384px"><svg viewBox="0 0 64 64" fill="none" stroke="#fff" stroke-width="3"><rect x="10" y="12" width="44" height="30" rx="2"/><path d="M24 52 H40 M32 42 V52"/></svg>IT</div>
  <div class="tile t-blue" style="top:326px;left:604px"><svg viewBox="0 0 64 64" fill="none" stroke="#fff" stroke-width="5"><circle cx="24" cy="36" r="10"/><circle cx="44" cy="18" r="7"/></svg>TECHNICAL</div>
  <div class="tile t-green" style="top:326px;left:827px"><svg viewBox="0 0 64 64"><path d="M6 50 L24 30 L34 40 L54 16" stroke="#fff" stroke-width="5" fill="none"/><path d="M44 14 H56 V26 Z" fill="#fff"/></svg>BUSINESS</div>
</section>

<section class="abs testi">
  <svg class="notch" style="top:-1px" viewBox="0 0 80 40"><path d="M0 0 Q40 0 40 40 Q40 0 80 0 Z" fill="#eceeee"/></svg>
  <h2>Our Testimonials</h2>
  <p class="quote-text">“ Sed ut perspiciatis unde omnis iste natus error sit voluptatem accusantium doloremque laudantium, totam rem aperiam, eaque ipsa quae ab illo inventore veritatis et quasi architecto beatae vitae dicta sunt explicabo. Nemo enim ipsam voluptatem quia voluptas sit aspernatur. ”</p>
  <p class="who">Head of Fulfillment, City Name</p>
  <div class="dots"><i></i><i></i><i></i><i></i></div>
</section>
<div class="avatar" role="img" aria-label="Portrait photo of the client giving the testimonial"></div>

<section class="abs news">
  <h2>Latest News</h2>
  <p class="lead">Sed ut perspiciatis unde omnis iste natus error sit voluptatem accusantium doloremque laudantium, totam rem aperiam, eaque ipsa quae ab illo inventore veritatis et quasi architecto beata.</p>
  <article class="card" style="left:160px">
    <div class="img" role="img" aria-label="Photo: team working at a desk with laptops and charts" style="background:linear-gradient(135deg,#c9b8a6,#7d6e62)"></div>
    <div class="share"><i></i><i></i><i></i></div>
    <h3>Framtiden för världens språk</h3>
    <p>At vivero eos et accusamus et iusto odio nocimusquiditate non provident, similique sunoto. Ifi cia deserunt mollita animi.</p>
    <div class="meta">▦ 20 FEB 2017 &nbsp;|&nbsp; ◯ Comments (00)</div>
  </article>
  <article class="card" style="left:463px">
    <div class="img" role="img" aria-label="Photo: plant growing from a jar of coins" style="background:linear-gradient(135deg,#c7b47a,#4d5a36)"></div>
    <div class="share"><i></i><i></i><i></i></div>
    <h3>Framtiden för världens språk</h3>
    <p>At vivero eos et accusamus et iusto odio nocimusquiditate non provident, similique sunoto. Ifi cia deserunt mollita animi.</p>
    <div class="meta">▦ 20 FEB 2017 &nbsp;|&nbsp; ◯ Comments (00)</div>
  </article>
  <article class="card" style="left:767px">
    <div class="img" role="img" aria-label="Photo: business handshake in a bright office" style="background:linear-gradient(135deg,#b9c6d2,#5e6e80)"></div>
    <div class="share"><i></i><i></i><i></i></div>
    <h3>Framtiden för världens språk</h3>
    <p>At vivero eos et accusamus et iusto odio nocimusquiditate non provident, similique sunoto. Ifi cia deserunt mollita animi.</p>
    <div class="meta">▦ 20 FEB 2017 &nbsp;|&nbsp; ◯ Comments (00)</div>
  </article>
</section>

<section class="abs partners" aria-label="Client partners">
  <i style="width:100px"></i><i style="width:110px"></i><i style="width:70px;height:40px"></i><i style="width:90px"></i><i style="width:100px"></i><i style="width:110px"></i>
</section>

<div class="abs rainbow" style="top:3773px;left:0;width:1200px"></div>
<footer class="abs footer">
  <div class="brand">verbanova<b></b></div>
  <p class="about-f">Verbanova is a translation agency that provides language services of the highest quality and maintains a strong focus on you, the customer.</p>
  <div class="col" style="left:408px"><h4>VERBANOVA AB</h4>Request a Quote<br>Contact<br>About Verbanova<br>VAT: SE559900112201</div>
  <div class="col" style="left:588px"><h4>TRANSLATION SERVICES</h4>Technical translations<br>Legal Translations<br>Financial translations<br>Medical translations</div>
  <div class="col" style="left:789px"><h4>ABOUT US</h4>News<br>About us<br>Contact us</div>
  <div class="col" style="left:925px"><h4>VERBANOVA AB</h4>Lindvägen 12,<br>SE 114 20, Stockholm<br>+46 (0)8 555 01 00</div>
  <div class="bottom"></div>
  <div class="soc"><i></i><i></i><i></i><i></i></div>
  <div class="copy"><span>© 2017 Verbanova. All Copyrights are Reserved.Terms of Use</span><span>Privacy Policy</span><span>Sitemap</span></div>
</footer>

</body>
</html>
```